Business Card Design

A business card design must match as a cleaning company.
We do house cleaning, office, cafe , function center , club and so on.

Industry/Entity Type

House

Contact Information for Business Card

Bright Lane cleaning services
Mara Delvin
Director
0428395146
1300 917 254
Brightlane.cleaning@bluvex.com

```html
<!DOCTYPE html>
<html lang="en">
<head>
<meta charset="UTF-8">
<title>Bright Lane Cleaning Services – Business Card</title>
<link rel="stylesheet" href="https://fonts.googleapis.com/css2?family=Montserrat:wght@400;500;700&display=swap">
<style>
  :root {
    --page-bg: #e4e5e7;
    --brand-blue: #1a7fc4;
    --brand-green: #5aa832;
    --card-white: #ffffff;
    --card-black: #1f1f21;
    --line-white: #ffffff;
  }
  * { margin: 0; padding: 0; box-sizing: border-box; }
  html, body { width: 1200px; height: 988px; overflow: hidden; }
  body {
    background: var(--page-bg);
    font-family: "Montserrat", sans-serif;
    display: flex;
    flex-direction: column;
    align-items: center;
    justify-content: center;
    gap: 40px;
  }
  .card {
    position: relative;
    width: 760px;
    height: 434px;
    overflow: hidden;
    box-shadow: 0 6px 18px rgba(0,0,0,0.18);
  }

  /* Front */
  .card--front {
    border: 12px solid var(--brand-green);
    background: var(--card-white);
  }
  .front-top {
    position: absolute;
    inset: 0 0 auto 0;
    height: 194px;
    background: linear-gradient(180deg, #ffffff 0%, #f1f4f6 100%);
  }
  .front-band {
    position: absolute;
    left: 0; right: 0; bottom: 0;
    height: 216px;
    background: var(--brand-blue);
  }
  .front-band .frame-corner {
    position: absolute;
    right: 26px; top: 26px; bottom: 26px;
    width: 40px;
    border: 2px solid var(--line-white);
    border-left: none;
  }
  .brand {
    position: absolute;
    display: flex;
    align-items: center;
    gap: 18px;
  }
  .brand--front { left: 60px; top: 58px; }
  .brand-dot {
    width: 62px; height: 62px;
    border-radius: 50%;
    background: var(--brand-blue);
    flex: none;
  }
  .brand-name {
    color: var(--brand-blue);
    font-weight: 700;
    text-transform: uppercase;
    line-height: 1.05;
  }
  .brand--front .brand-name { font-size: 36px; letter-spacing: 2px; }
  .brand-name small { display: block; font-size: 0.5em; letter-spacing: 4px; }

  .contact {
    position: absolute;
    left: 60px; right: 100px; top: 222px;
    color: var(--line-white);
  }
  .person { font-size: 22px; font-weight: 700; letter-spacing: 2px; text-transform: uppercase; }
  .role { font-size: 13px; font-weight: 500; letter-spacing: 3px; text-transform: uppercase; margin-top: 4px; }
  .details {
    display: grid;
    grid-template-columns: 1fr 1fr;
    gap: 10px 24px;
    margin-top: 22px;
    font-size: 14px;
    font-weight: 400;
    line-height: 18px;
  }
  .detail { display: flex; align-items: center; gap: 10px; white-space: nowrap; }
  .detail svg { width: 18px; height: 18px; flex: none; }
  .detail--wide { grid-column: 1 / -1; }

  /* Back */
  .card--back {
    border: 16px solid var(--brand-blue);
    background: var(--card-black);
  }
  .corner {
    position: absolute;
    width: 90px; height: 70px;
    border: 2px solid var(--line-white);
  }
  .corner--tr { top: 22px; right: 22px; border-left: none; border-bottom: none; }
  .corner--bl { bottom: 22px; left: 22px; border-right: none; border-top: none; }
  .brand--back {
    left: 50%; top: 50%;
    transform: translate(-50%, -50%);
    flex-direction: column;
    text-align: center;
    gap: 16px;
  }
  .brand--back .brand-dot { width: 54px; height: 54px; }
  .brand--back .brand-name { font-size: 44px; letter-spacing: 3px; white-space: nowrap; }
</style>
</head>
<body>

  <section class="card card--front" aria-label="Business card front">
    <div class="front-top"></div>
    <div class="front-band"><span class="frame-corner"></span></div>

    <div class="brand brand--front">
      <span class="brand-dot"></span>
      <div class="brand-name">Bright Lane<small>Cleaning Services</small></div>
    </div>

    <div class="contact">
      <p class="person">Mara Delvin</p>
      <p class="role">Director</p>
      <div class="details">
        <p class="detail">
          <svg viewBox="0 0 24 24" aria-hidden="true"><circle cx="12" cy="12" r="12" fill="#fff"/><path d="M8 6.5l2 0 1 3-1.4 1.2a8 8 0 0 0 3.7 3.7L14.5 13l3 1v2a1.5 1.5 0 0 1-1.6 1.5A10 10 0 0 1 6.5 8.1 1.5 1.5 0 0 1 8 6.5z" fill="#1a7fc4"/></svg>
          0491 570 156
        </p>
        <p class="detail">
          <svg viewBox="0 0 24 24" aria-hidden="true"><circle cx="12" cy="12" r="12" fill="#fff"/><path d="M8 6.5l2 0 1 3-1.4 1.2a8 8 0 0 0 3.7 3.7L14.5 13l3 1v2a1.5 1.5 0 0 1-1.6 1.5A10 10 0 0 1 6.5 8.1 1.5 1.5 0 0 1 8 6.5z" fill="#1a7fc4"/></svg>
          1300 975 707
        </p>
        <p class="detail">
          <svg viewBox="0 0 24 24" aria-hidden="true"><circle cx="12" cy="12" r="12" fill="#fff"/><rect x="6" y="8" width="12" height="8" fill="none" stroke="#1a7fc4" stroke-width="1.6"/><path d="M6 8l6 5 6-5" fill="none" stroke="#1a7fc4" stroke-width="1.6"/></svg>
          brightlane.cleaning@example.com
        </p>
        <p class="detail">
          <svg viewBox="0 0 24 24" aria-hidden="true"><circle cx="12" cy="12" r="12" fill="#fff"/><circle cx="12" cy="12" r="6" fill="none" stroke="#1a7fc4" stroke-width="1.6"/><path d="M6 12h12M12 6c-3 3.5-3 8.5 0 12M12 6c3 3.5 3 8.5 0 12" fill="none" stroke="#1a7fc4" stroke-width="1.2"/></svg>
          www.brightlane.example
        </p>
        <p class="detail detail--wide">
          <svg viewBox="0 0 24 24" aria-hidden="true"><circle cx="12" cy="12" r="12" fill="#fff"/><path d="M12 5a4.5 4.5 0 0 0-4.5 4.5C7.5 13 12 19 12 19s4.5-6 4.5-9.5A4.5 4.5 0 0 0 12 5z" fill="#1a7fc4"/><circle cx="12" cy="9.5" r="1.6" fill="#fff"/></svg>
          14 Harbour Street, Lakeside Park
        </p>
      </div>
    </div>
  </section>

  <section class="card card--back" aria-label="Business card back">
    <span class="corner corner--tr"></span>
    <span class="corner corner--bl"></span>
    <div class="brand brand--back">
      <span class="brand-dot"></span>
      <div class="brand-name">Bright Lane<small>Cleaning Services</small></div>
    </div>
  </section>

</body>
</html>
```